Lantern Keepers Lantern Scribes

We would like the business card to be Horizontal
Logo on the back and want it raised.

Target Market(s)

Education and Museums

Industry/Entity Type

Education

Contact Information for Business Card

Dolores Wrenfield, P.H.D.
3918 Pelham Rd
Ashford, VT 05347
612.447.3095
Dolores.Wrenfield@lanternkeeperslanternscribes.org
lanternkeeperslanternscribes.org

Font styles to use
Serif

Colors

Designer to choose colors to be used in the design.

Requirements
Must have
• letters and logo must be raised
• Must be slate blue card
• Silver is aluminum foil

```html
<!DOCTYPE html>
<html lang="en">
<head>
<meta charset="utf-8">
<title>Lantern Keepers Lantern Scribes — Business Card</title>
<link rel="stylesheet" href="https://fonts.googleapis.com/css2?family=Noto+Serif:wght@400;700&display=swap">
<style>
  :root {
    --backdrop: #b8bfcc;
    --card-navy: #1b2a55;
    --card-navy-deep: #16234a;
    --accent-orange: #e07c22;
    --foil-silver: #cfd2d8;
    --text-white: #ffffff;
  }
  * { box-sizing: border-box; margin: 0; padding: 0; }
  html, body {
    width: 1200px; height: 1200px; overflow: hidden;
    background: var(--backdrop);
    font-family: "Noto Serif", Georgia, serif;
  }
  .canvas { position: relative; width: 1200px; height: 1200px; }
  .card {
    position: absolute; left: 188px; width: 825px; height: 518px;
    border-radius: 31px; overflow: hidden;
    background: linear-gradient(135deg, var(--card-navy) 0%, var(--card-navy-deep) 100%);
  }
  .card--front { top: 60px; }
  .card--back { top: 622px; }
  .card__band {
    position: absolute; left: 0; right: 0; bottom: 0; height: 26px;
    background: var(--accent-orange);
  }
  .brand-mark {
    position: absolute; text-align: center;
    color: var(--foil-silver); font-weight: 700; line-height: 1.2;
    white-space: nowrap;
  }
  .card--front .brand-mark {
    left: 0; right: 0; top: 196px; font-size: 44px;
  }
  .card--back .brand-mark {
    left: 590px; width: 190px; top: 112px; font-size: 21px;
  }
  .holder__name {
    position: absolute; left: 73px; top: 92px;
    color: var(--text-white); font-weight: 700; font-size: 36px; white-space: nowrap;
  }
  .holder__title {
    position: absolute; left: 73px; top: 140px;
    color: var(--accent-orange); font-weight: 400; font-size: 30px;
  }
  .contact-list { position: absolute; left: 70px; top: 220px; list-style: none; }
  .contact-list__item {
    position: relative; padding-left: 47px; color: var(--text-white);
    font-size: 22px; line-height: 31px; margin-bottom: 18px; letter-spacing: 0.3px;
    white-space: nowrap;
  }
  .contact-list__icon {
    position: absolute; left: 0; top: 1px; width: 30px; height: 30px;
  }
  .contact-list__item--address { margin-top: -4px; }
</style>
</head>
<body>
<main class="canvas">
  <section class="card card--front" aria-label="Card front">
    <div class="brand-mark">Lantern Keepers<br>Lantern Scribes</div>
    <div class="card__band"></div>
  </section>

  <section class="card card--back" aria-label="Card back">
    <h1 class="holder__name">Dolores Wrenfield, P.H.D.</h1>
    <p class="holder__title">Principal</p>

    <ul class="contact-list">
      <li class="contact-list__item">
        <svg class="contact-list__icon" viewBox="0 0 30 30" aria-hidden="true">
          <circle cx="15" cy="15" r="15" fill="#e07c22"/>
          <path d="M10.5 8.5l2.5-.5 1.6 3.6-1.6 1.2c.8 1.8 2.2 3.2 4 4l1.2-1.6 3.6 1.6-.5 2.5c-.3.8-1 1.2-1.8 1.1-5.3-.7-9.4-4.8-10.1-10.1-.1-.8.3-1.5 1.1-1.8z" fill="#1b2a55"/>
        </svg>
        612.447.3095
      </li>
      <li class="contact-list__item">
        <svg class="contact-list__icon" viewBox="0 0 30 30" aria-hidden="true">
          <circle cx="15" cy="15" r="15" fill="#e07c22"/>
          <rect x="8" y="10" width="14" height="10" fill="none" stroke="#1b2a55" stroke-width="1.3"/>
          <path d="M8 10l7 6 7-6M8 20l5-5M22 20l-5-5" fill="none" stroke="#1b2a55" stroke-width="1.3"/>
        </svg>
        Dolores.Wrenfield@lanternkeeperslanternscribes.org
      </li>
      <li class="contact-list__item">
        <svg class="contact-list__icon" viewBox="0 0 30 30" aria-hidden="true">
          <circle cx="15" cy="15" r="15" fill="#e07c22"/>
          <g fill="none" stroke="#1b2a55" stroke-width="1.3">
            <circle cx="15" cy="15" r="8"/><ellipse cx="15" cy="15" rx="3.5" ry="8"/>
            <path d="M7 15h16M8.2 11h13.6M8.2 19h13.6"/>
          </g>
        </svg>
        lanternkeeperslanternscribes.org
      </li>
      <li class="contact-list__item contact-list__item--address">
        <svg class="contact-list__icon" viewBox="0 0 30 30" aria-hidden="true">
          <circle cx="15" cy="15" r="15" fill="#e07c22"/>
          <g fill="none" stroke="#1b2a55" stroke-width="1.3">
            <circle cx="15" cy="15" r="8"/><ellipse cx="15" cy="15" rx="3.5" ry="8"/>
            <path d="M7 15h16M8.2 11h13.6M8.2 19h13.6"/>
          </g>
        </svg>
        3918 Pelham Rd<br>Ashford, VT 05347
      </li>
    </ul>

    <div class="brand-mark">Lantern Keepers<br>Lantern Scribes</div>
    <div class="card__band"></div>
  </section>
</main>
</body>
</html>
```